Business Cards for new orthopaedic surgery practice

My husband and I are starting our own orthopaedic surgery practice. We are looking for a business card that is uniform, but one will have my name/title and the other will have his. You can just create one design with my name on it for now. But when I choose your design as the winning design I will ask that you add another copy with his name/title.

We are looking for classy, simple, elite all in one. We like dark blues/a little gold/yellow. Something that goes with our logo. We want our logo incorporated. Here is all the info you need:
Business name: RV Spine & Vitality Center
Location: 38915 North Bramble Ave
Palm Verde, FL 33998
Phone: 954-218-4630
Fax: 954-571-2846
Email: info@myrvspine.example

Names: Lucinda Ferrow, M.D.
Board Certified Hand and Upper Extremity Surgeon

Emeka Dlunga, M.D.
Board Certified Hip & Knee Replacement/General Orthopaedic Surgeon

Can decide what you want to put on the back. Maybe a slogan:
Steady Hands. Strength for You

I am just going to upload our logo. The only thing is if we select you as the winning design, the location, and phone numbers may change. We will need your help to update that once fully solidified.

Industry/Entity Type

Medical

Contact Information for Business Card

Colors
0054AA
0677BA
7BADD7
CADEEF
E8F1F8
0094D4
00A9DD
6FCCEA
C7EBF8
E9F6FB

Requirements
Must have
• class, appeal,
Should not have
• We want to air on the side of masculine if we are looking at masculine vs. feminine feel. But we still want it classy, sophisticated, and something we will love

```html
<!DOCTYPE html>
<html lang="en">
<head>
<meta charset="utf-8">
<title>RV Spine &amp; Vitality Center — Business Card</title>
<link href="https://fonts.googleapis.com/css2?family=Cinzel:wght@400;600&family=Crimson+Text:wght@400;600&display=swap" rel="stylesheet">
<style>
  :root {
    --backdrop: #3a3a3c;
    --card-navy: #233d80;
    --ink-white: #ffffff;
    --accent-cyan: #00a9dd;
    --rule-white: rgba(255,255,255,0.9);
  }
  * { margin: 0; padding: 0; box-sizing: border-box; }
  html, body { width: 1200px; height: 694px; overflow: hidden; background: var(--backdrop); }
  .canvas { position: relative; width: 1200px; height: 694px; }

  .card {
    position: absolute;
    width: 540px; height: 309px;
    background: var(--card-navy);
    border-radius: 16px;
    color: var(--ink-white);
    box-shadow: 0 12px 30px rgba(0,0,0,0.45);
    overflow: hidden;
  }
  .card--front { left: 50px; top: 90px; }
  .card--back  { left: 610px; top: 295px; }

  /* Front */
  .front-brand {
    position: absolute; left: 0; right: 0; top: 84px;
    text-align: center;
  }
  .brand-name {
    font-family: "Cinzel", serif;
    font-weight: 600;
    color: var(--ink-white);
  }
  .front-brand .brand-name { font-size: 30px; line-height: 1.15; letter-spacing: 0.5px; }
  .front-brand .brand-mark {
    display: inline-block; width: 14px; height: 14px; border-radius: 50%;
    background: var(--accent-cyan); margin-bottom: 14px;
  }
  .front-rule {
    width: 260px; height: 1px; background: var(--rule-white);
    margin: 14px auto 0;
  }
  .slogan {
    position: absolute; left: 0; right: 0; bottom: 56px;
    text-align: center;
    font-family: "Cinzel", serif; font-size: 14px; letter-spacing: 5px;
  }

  /* Back */
  .back-brand {
    position: absolute; right: 36px; top: 30px;
    display: flex; align-items: center; gap: 10px;
  }
  .back-brand .brand-mark { width: 10px; height: 10px; border-radius: 50%; background: var(--accent-cyan); flex: none; }
  .back-brand .brand-name { font-size: 15px; line-height: 1.2; text-align: left; max-width: 190px; }

  .person { position: absolute; left: 36px; top: 112px; }
  .person-name {
    font-family: "Cinzel", serif; font-weight: 600; font-size: 18px;
    color: var(--accent-cyan); letter-spacing: 0.5px;
  }
  .person-title {
    font-family: "Crimson Text", serif; font-weight: 600; font-size: 13px; line-height: 1.2;
    margin-top: 4px;
  }

  .hours {
    position: absolute; right: 36px; top: 124px; text-align: right;
    font-family: "Crimson Text", serif; font-size: 13px; line-height: 1.3;
  }
  .hours-closed { color: var(--accent-cyan); }

  .contact {
    position: absolute; left: 36px; bottom: 24px;
    font-family: "Crimson Text", serif; font-weight: 600; font-size: 13px; line-height: 1.3;
  }
  .address { margin-bottom: 10px; }
  .contact-list { list-style: none; }
  .contact-list li { display: flex; align-items: center; gap: 8px; }
  .contact-icon { width: 12px; height: 12px; fill: var(--accent-cyan); flex: none; }
</style>
</head>
<body>
<main class="canvas">

  <section class="card card--front" aria-label="Card front">
    <div class="front-brand">
      <span class="brand-mark"></span>
      <div class="brand-name">RV Spine &amp; Vitality<br>Center</div>
      <div class="front-rule"></div>
    </div>
    <p class="slogan">STEADY HANDS. STRENGTH FOR YOU</p>
  </section>

  <section class="card card--back" aria-label="Card back">
    <div class="back-brand">
      <span class="brand-mark"></span>
      <div class="brand-name">RV Spine &amp; Vitality Center</div>
    </div>

    <div class="person">
      <h1 class="person-name">LUCINDA FERROW, M.D.</h1>
      <p class="person-title">Board Certified Hand<br>and Upper Extremity Surgeon</p>
    </div>

    <div class="hours">
      <p>Opening Hours</p>
      <p>Monday to Friday - 9:00 AM - 5:00 PM</p>
      <p class="hours-closed">Saturday / Sunday Closed</p>
    </div>

    <div class="contact">
      <p class="address">38915 North Bramble Ave<br>Palm Verde, FL 33998</p>
      <ul class="contact-list">
        <li>
          <svg class="contact-icon" viewBox="0 0 24 24" aria-hidden="true"><path d="M6.6 10.8a15.1 15.1 0 0 0 6.6 6.6l2.2-2.2a1 1 0 0 1 1-.25 11.4 11.4 0 0 0 3.6.57 1 1 0 0 1 1 1V20a1 1 0 0 1-1 1A17 17 0 0 1 3 4a1 1 0 0 1 1-1h3.5a1 1 0 0 1 1 1c0 1.25.2 2.45.57 3.6a1 1 0 0 1-.25 1z"/></svg>
          <span>954-218-4630</span>
        </li>
        <li>
          <svg class="contact-icon" viewBox="0 0 24 24" aria-hidden="true"><path d="M6 2h12v6H6zM3 9h18a1 1 0 0 1 1 1v7h-4v5H6v-5H2v-7a1 1 0 0 1 1-1zm5 7v4h8v-4z"/></svg>
          <span>954-571-2846</span>
        </li>
        <li>
          <svg class="contact-icon" viewBox="0 0 24 24" aria-hidden="true"><path d="M2 5h20v14H2zm2 2v.5l8 5 8-5V7l-8 5z"/></svg>
          <span>info@myrvspine.example</span>
        </li>
      </ul>
    </div>
  </section>

</main>
</body>
</html>
```